Letterhead/Envelope/Business Cards for law firm - Marlowe & Tesniere PLLC
Marlowe Tesniere
Letterhead/Envelope/Business Cards for law firm - Marlowe & Tesniere PLLC - Law
Creative Brief
Use same font as used in my logo
Open to any ideas
Simple
Doran P. Tesniere
Attorney
Marlowe & Tesniere PLLC 618 Briarmoss Court Plaza 375 North Galloway Avenue Louisville, Kentucky 40597
dtesniere@mtlegalgroup.example
www.mtlegalgroup.example
Licensed in Kentucky, Indiana & West Virginia
We are looking for design of letterhead, envelopes and business cards.
We want to use our logo. But we also need Marlowe & Tesniere, PLLC on the card/letterhead.

```html
<!DOCTYPE html>
<html lang="en">
<head>
<meta charset="utf-8">
<title>Marlowe &amp; Tesniere PLLC — Stationery Concepts</title>
<link rel="stylesheet" href="https://fonts.googleapis.com/css2?family=Raleway:wght@400;600&display=swap">
<style>
  :root {
    --backdrop: #e6d7c1;
    --paper: #ffffff;
    --brand-red: #c4142b;
    --brand-black: #161616;
    --ink: #3a3a3a;
    --label: #6b5a45;
    --faint: #ececec;
  }
  * { box-sizing: border-box; margin: 0; padding: 0; }
  html, body { width: 1200px; height: 446px; overflow: hidden; }
  body {
    background: var(--backdrop);
    font-family: "Raleway", Arial, sans-serif;
    color: var(--ink);
    position: relative;
  }
  .sheet-label {
    position: absolute;
    font-size: 5.5px;
    letter-spacing: .8px;
    text-transform: uppercase;
    color: var(--label);
    white-space: nowrap;
  }
  .item {
    position: absolute;
    background: var(--paper);
    box-shadow: 0 2px 5px rgba(0,0,0,.25);
    overflow: hidden;
  }
  .wordmark {
    display: flex;
    align-items: center;
    gap: 3px;
    font-weight: 600;
    color: var(--brand-black);
    letter-spacing: .5px;
    text-transform: uppercase;
    white-space: nowrap;
  }
  .wordmark .mark {
    display: inline-block;
    background: var(--brand-red);
  }
  .contact {
    position: absolute;
    font-size: 3.2px;
    line-height: 1.35;
    color: var(--ink);
  }
  .wave { position: absolute; left: 0; bottom: 0; width: 100%; display: block; }

  /* business cards */
  .card { width: 113px; height: 62px; left: 12px; }
  .card-front { top: 150px; }
  .card-back  { top: 240px; display: flex; align-items: center; justify-content: center; }
  .card-front .wordmark { position: absolute; left: 8px; top: 22px; font-size: 6px; }
  .card-front .wordmark .mark { width: 6px; height: 6px; }
  .card-back .wordmark { font-size: 6px; }
  .card-back .wordmark .mark { width: 7px; height: 7px; }

  /* letterheads */
  .letterhead { width: 210px; height: 415px; top: 12px; }
  .letterhead-one { left: 247px; }
  .letterhead-two { left: 475px; }
  .letterhead .wordmark { position: absolute; left: 16px; top: 20px; font-size: 6.5px; }
  .letterhead .wordmark .mark { width: 7px; height: 7px; }
  .letterhead .contact { left: 112px; top: 18px; }
  .faint-name {
    position: absolute;
    left: 0; right: 0; top: 185px;
    text-align: center;
    font-size: 15px;
    font-weight: 600;
    letter-spacing: 2px;
    text-transform: uppercase;
    color: var(--faint);
  }

  /* envelopes */
  .envelope-inside { left: 804px; top: 22px; width: 325px; height: 80px; }
  .envelope-inside .liner { height: 22px; background: var(--brand-red); }
  .envelope-open { left: 804px; top: 100px; width: 325px; height: 62px; background: var(--brand-black); }
  .envelope-back { left: 804px; top: 170px; width: 325px; height: 82px; }
  .envelope-back .wordmark { position: absolute; left: 50%; top: 46px; transform: translateX(-50%); font-size: 6px; }
  .envelope-back .wordmark .mark { width: 7px; height: 7px; }
  .envelope-front { left: 795px; top: 262px; width: 334px; height: 158px; }
  .envelope-front .wordmark { position: absolute; left: 14px; top: 16px; font-size: 6.5px; }
  .envelope-front .wordmark .mark { width: 7px; height: 7px; }
  .envelope-front .contact { left: 14px; top: 28px; }
</style>
</head>
<body>

  <p class="sheet-label" style="left:12px; top:118px;">Stationery Concepts</p>

  <section class="item card card-front" aria-label="Business card front">
    <div class="wordmark"><span class="mark"></span>Marlowe Tesniere</div>
    <svg class="wave" viewBox="0 0 113 18" preserveAspectRatio="none">
      <path d="M0,8 C35,0 70,16 113,4 L113,18 L0,18Z" fill="var(--brand-black)"/>
      <path d="M0,11 C35,4 70,19 113,8 L113,18 L0,18Z" fill="var(--brand-red)"/>
    </svg>
  </section>
  <p class="sheet-label" style="left:34px; top:218px;">Business Card Front</p>

  <section class="item card card-back" aria-label="Business card back">
    <div class="wordmark"><span class="mark"></span>Marlowe Tesniere</div>
  </section>
  <p class="sheet-label" style="left:36px; top:310px;">Business Card Back</p>

  <section class="item letterhead letterhead-one" aria-label="Letterhead option 1">
    <div class="wordmark"><span class="mark"></span>Marlowe &amp; Tesniere</div>
    <div class="contact">
      Marlowe &amp; Tesniere, PLLC<br>
      618 Briarmoss Court Plaza<br>
      375 North Galloway Avenue<br>
      Louisville, Kentucky 40597<br>
      www.mtlegalgroup.example
    </div>
    <svg class="wave" viewBox="0 0 210 70" preserveAspectRatio="none">
      <path d="M0,14 C70,-4 130,40 210,12 L210,70 L0,70Z" fill="#cfcfcf"/>
      <path d="M0,20 C70,2 130,46 210,18 L210,70 L0,70Z" fill="var(--brand-black)"/>
      <path d="M0,28 C70,12 130,54 210,28 L210,70 L0,70Z" fill="var(--brand-red)"/>
    </svg>
  </section>
  <p class="sheet-label" style="left:320px; top:432px;">Letterhead Option 1</p>

  <section class="item letterhead letterhead-two" aria-label="Letterhead option 2">
    <div class="wordmark"><span class="mark"></span>Marlowe &amp; Tesniere</div>
    <div class="contact">
      Marlowe &amp; Tesniere, PLLC<br>
      618 Briarmoss Court Plaza<br>
      375 North Galloway Avenue<br>
      Louisville, Kentucky 40597<br>
      www.mtlegalgroup.example
    </div>
    <p class="faint-name">Marlowe Tesniere</p>
    <svg class="wave" viewBox="0 0 210 70" preserveAspectRatio="none">
      <path d="M0,14 C70,-4 130,40 210,12 L210,70 L0,70Z" fill="#cfcfcf"/>
      <path d="M0,20 C70,2 130,46 210,18 L210,70 L0,70Z" fill="var(--brand-black)"/>
      <path d="M0,28 C70,12 130,54 210,28 L210,70 L0,70Z" fill="var(--brand-red)"/>
    </svg>
  </section>
  <p class="sheet-label" style="left:548px; top:432px;">Letterhead Option 2</p>

  <section class="item envelope-inside" aria-label="Envelope inside liner">
    <div class="liner"></div>
  </section>

  <section class="item envelope-open" aria-label="Open envelope">
    <svg width="325" height="62" viewBox="0 0 325 62">
      <path d="M0,0 L162,40 L325,0 L325,6 L162,48 L0,6Z" fill="var(--paper)"/>
    </svg>
  </section>

  <section class="item envelope-back" aria-label="Envelope back">
    <svg width="325" height="82" viewBox="0 0 325 82">
      <path d="M0,0 L162,38 L325,0" fill="none" stroke="#d4d4d4" stroke-width="1"/>
    </svg>
    <div class="wordmark"><span class="mark"></span>Marlowe Tesniere</div>
  </section>

  <section class="item envelope-front" aria-label="Envelope front">
    <div class="wordmark"><span class="mark"></span>Marlowe &amp; Tesniere</div>
    <div class="contact">
      618 Briarmoss Court Plaza<br>
      375 North Galloway Avenue<br>
      Louisville, Kentucky 40597
    </div>
    <svg class="wave" viewBox="0 0 334 40" preserveAspectRatio="none">
      <path d="M0,10 C110,-2 200,26 334,8 L334,40 L0,40Z" fill="var(--brand-black)"/>
      <path d="M0,16 C110,5 200,32 334,15 L334,40 L0,40Z" fill="var(--brand-red)"/>
    </svg>
  </section>
  <p class="sheet-label" style="left:935px; top:432px;">Envelope Option 1</p>

</body>
</html>
```